Business Card Design

We need a business card design for a new company (Sole Proprietorship) based in Maryland,USA. We sell African wears & fabrics, headgears, trendy clothes, shoes and accessories.
We cater for men's and women's needs and we sell retail.
We would like to see designs that use a beautiful arrays of colors- The final design design should communicate FASHION.
Industry/Entity Type
Business
Contact Information for Business Card
Name: Folasade Okonkwo
Name of Business: Patterns & Hues
Address: 27481 Briarstone Court, Laurel, MD 20934
Telephone: 240-731-5096
E-mail: patternsandhues@mailvexo.com
Look and feel
Each slider illustrates characteristics of the customer's brand and the style your logo design should communicate.

```html
<!DOCTYPE html>
<html lang="en">
<head>
<meta charset="utf-8">
<title>Patterns &amp; Hues — Business Card</title>
<link rel="stylesheet" href="https://fonts.googleapis.com/css2?family=Orbitron:wght@700&family=Play:wght@400;700&display=swap">
<style>
  :root {
    --bg: #e9e9e7;
    --paper: #ffffff;
    --brand-blue: #1aa9e0;
    --band-blue: #0aaeea;
    --silver-light: #f4f4f4;
    --silver-mid: #d6d6d6;
    --graphite: #5b5b5b;
    --graphite-dark: #2e2e2e;
    --ink: #2b2b2b;
    --white: #ffffff;
  }
  * { box-sizing: border-box; margin: 0; padding: 0; }
  html, body { width: 1200px; height: 869px; overflow: hidden; }
  body { background: var(--bg); position: relative; font-family: "Play", sans-serif; }

  .card {
    position: absolute;
    width: 520px;
    height: 297px;
    overflow: hidden;
    box-shadow: 0 6px 18px rgba(0,0,0,.18);
  }
  .card--front { left: 50px; top: 286px; background: var(--paper); }
  .card--back { left: 630px; top: 286px; background: linear-gradient(160deg, var(--silver-light) 0%, var(--silver-mid) 100%); }

  .wordmark {
    font-family: "Orbitron", sans-serif;
    font-weight: 700;
    color: var(--brand-blue);
    letter-spacing: 1px;
  }
  .card--front .wordmark {
    position: absolute; left: 0; right: 0; top: 126px;
    text-align: center; font-size: 34px;
  }
  .card--back .wordmark {
    position: absolute; left: 22px; top: 22px;
    font-size: 22px; line-height: 30px;
  }

  .band {
    position: absolute; left: 0; width: 100%;
    top: 112px; height: 140px;
    background: var(--band-blue);
  }
  .base-strip {
    position: absolute; left: 0; width: 100%;
    top: 252px; height: 45px;
    background: linear-gradient(90deg, var(--graphite-dark) 0%, #7c7c7c 45%, var(--graphite) 70%, var(--graphite-dark) 100%);
  }
  .ribbon { position: absolute; left: 120px; top: 100px; width: 400px; height: 36px; }
  .ribbon__text {
    position: absolute; left: 150px; top: 107px;
    color: var(--white); font-size: 13px; letter-spacing: .3px;
  }

  .holder { position: absolute; right: 26px; top: 50px; text-align: right; color: var(--ink); }
  .holder__name { font-size: 19px; font-weight: 400; letter-spacing: 1px; }
  .holder__role { font-size: 10px; letter-spacing: 1px; text-transform: uppercase; }

  .contact { position: absolute; display: flex; align-items: center; gap: 9px; color: var(--white); font-size: 12.5px; }
  .contact__icon { width: 20px; height: 20px; background: var(--white); border-radius: 3px; flex: none; }
  .contact--web { left: 22px; top: 148px; }
  .contact--mail { left: 22px; top: 178px; }
  .contact--phone { left: 300px; top: 194px; font-size: 13px; letter-spacing: 1px; }
  .contact--mobile { left: 300px; top: 222px; font-size: 13px; letter-spacing: 1px; }
</style>
</head>
<body>

  <section class="card card--front" aria-label="Card front">
    <div class="wordmark">Patterns &amp; Hues</div>
  </section>

  <section class="card card--back" aria-label="Card back">
    <div class="wordmark">Patterns<br>&amp; Hues</div>

    <div class="holder">
      <div class="holder__name">FOLASADE OKONKWO</div>
      <div class="holder__role">General Manager</div>
    </div>

    <div class="band"></div>

    <svg class="ribbon" viewBox="0 0 400 36" aria-hidden="true">
      <polygon points="0,0 340,0 330,12 400,12 400,36 10,36" fill="#6a6a6a"/>
      <polygon points="0,0 10,36 10,12" fill="#4a4a4a"/>
    </svg>
    <div class="ribbon__text">27481 Briarstone Court, MD 20934</div>

    <div class="contact contact--web">
      <svg class="contact__icon" viewBox="0 0 20 20" aria-hidden="true">
        <rect width="20" height="20" rx="3" fill="#fff"/>
        <circle cx="10" cy="10" r="6" fill="none" stroke="#0aaeea" stroke-width="1.4"/>
        <ellipse cx="10" cy="10" rx="2.6" ry="6" fill="none" stroke="#0aaeea" stroke-width="1.2"/>
        <line x1="4" y1="10" x2="16" y2="10" stroke="#0aaeea" stroke-width="1.2"/>
      </svg>
      <span>www.patternsandhues.shop</span>
    </div>
    <div class="contact contact--mail">
      <svg class="contact__icon" viewBox="0 0 20 20" aria-hidden="true">
        <rect width="20" height="20" rx="3" fill="#fff"/>
        <rect x="4" y="6" width="12" height="8" fill="none" stroke="#0aaeea" stroke-width="1.4"/>
        <polyline points="4,6 10,11 16,6" fill="none" stroke="#0aaeea" stroke-width="1.4"/>
      </svg>
      <span>patternsandhues@mailvexo.com</span>
    </div>
    <div class="contact contact--phone">
      <svg class="contact__icon" viewBox="0 0 20 20" aria-hidden="true">
        <rect width="20" height="20" rx="3" fill="#fff"/>
        <path d="M7 4 L9 4 L9.5 7 L8.3 8 Q9.5 11 12 12 L13 10.8 L16 11.3 L16 13.5 Q10 15 6.5 9 Q5.5 6 7 4 Z" fill="#0aaeea"/>
      </svg>
      <span>240-731-5096</span>
    </div>
    <div class="contact contact--mobile">
      <svg class="contact__icon" viewBox="0 0 20 20" aria-hidden="true">
        <rect width="20" height="20" rx="3" fill="#fff"/>
        <rect x="6.5" y="3.5" width="7" height="13" rx="1.2" fill="none" stroke="#0aaeea" stroke-width="1.4"/>
        <circle cx="10" cy="14" r=".9" fill="#0aaeea"/>
      </svg>
      <span>240-731-5096</span>
    </div>

    <div class="base-strip"></div>
  </section>

</body>
</html>
```